New Website for ReBranded Company - CrewBeacon

We have a successful company and website currently but it is a little dated. We have re-branded the company from Harbor Signal Networks to CrewBeacon and have a new logo for the new name. We are looking to build a newer fresher website with the new name. I will need a concept of the home page and one inside page. You can see our current site at https://www.harborsignalnetworks.example and the new site will be https://www.crewbeacon.example .

I also really like the https://www.pathmolder.example/ website. I like ledgerleaf.example website. I like the https://skillbinder.example/ website.

See the attached document for layout and some text to use. Use the pictures I attached as opposed to pictures from the old site as much as you can.

Target Market(s)

Business

Industry/Entity Type

Software Service

Number of Pages Required

2 page

Font styles to use
Sans Serif

Requirements
Must have
• Use the colors from my logo. Professional but modern. We want people to feel like our product makes their staff feel safer at work.
Should not have
• Don't use any red or orange (no stop colors).

```html
<!DOCTYPE html>
<html lang="en">
<head>
<meta charset="utf-8">
<title>CrewBeacon – Get Help Fast</title>
<link href="https://fonts.googleapis.com/css2?family=Open+Sans:wght@400;600;700&family=Roboto:wght@400;500;700&display=swap" rel="stylesheet">
<style>
:root{
  --blue:#1f7fc6;
  --blue-dark:#176db3;
  --blue-light:#3596d8;
  --navy:#134a7c;
  --sky:#bfe0f7;
  --ink:#333a40;
  --muted:#6b7075;
  --line:#1f7fc6;
  --white:#ffffff;
  --pale:#f4f6f8;
  --note:#eef5fb;
}
*{box-sizing:border-box;margin:0;padding:0}
html,body{width:1200px;height:3728px;overflow:hidden}
body{font-family:"Open Sans",sans-serif;color:var(--ink);background:var(--white);position:relative}
.abs{position:absolute}
.btn{position:absolute;display:flex;align-items:center;justify-content:center;font-family:"Roboto",sans-serif;font-weight:700;font-size:16px;border-radius:2px;text-decoration:none}
.btn-solid{background:var(--blue);color:var(--white)}
.btn-white{background:var(--white);color:var(--blue)}
.band{background:linear-gradient(180deg,var(--blue-light),var(--blue-dark));color:var(--white)}

/* header */
.site-header{position:absolute;left:0;top:0;width:1200px;height:67px;background:var(--white)}
.brand{position:absolute;display:flex;align-items:center;gap:8px;font-family:"Open Sans",sans-serif;font-weight:700;color:var(--blue)}
.brand .dot{border-radius:50%;background:var(--blue)}
.nav a{position:absolute;top:22px;font-family:"Roboto",sans-serif;font-size:15px;color:var(--blue);text-decoration:none}
.nav .active{border-bottom:2px solid var(--blue);padding-bottom:10px}
.btn-outline{border:1.5px solid var(--blue);color:var(--blue);font-weight:500;background:var(--white)}

/* hero */
.hero-photo{left:0;top:67px;width:1200px;height:450px;background:linear-gradient(135deg,#8a8e90 0%,#5e5a55 35%,#b8c0b0 70%,#d8dcd6 100%)}
.hero-band{left:0;top:517px;width:1200px;height:158px;text-align:center}
.hero-band h1{position:absolute;top:6px;width:100%;font-size:40px;line-height:52px;font-weight:700;letter-spacing:.3px}
.hero-band p{position:absolute;top:56px;width:100%;font-family:"Roboto",sans-serif;font-weight:700;font-size:16px;line-height:20px}

/* features */
.feature{position:absolute;top:700px;width:230px;text-align:center}
.feature svg,.feature .ph{display:block;margin:0 auto;height:90px}
.feature hr{border:0;border-top:2px solid var(--line);width:210px;margin:10px auto 16px}
.feature p{font-size:14.5px;line-height:20px;color:var(--muted);width:200px;margin:0 auto}

/* employees */
.pocket-photo{left:766px;top:938px;width:434px;height:536px;background:linear-gradient(160deg,#8f8a82 0%,#3d4f6e 45%,#24365a 100%)}
.emp-title{left:150px;top:998px;font-size:31px;font-weight:600;line-height:45px;color:var(--ink)}
.emp-q{left:146px;top:1112px;font-size:19px;line-height:27px;width:420px}
.emp-q2{left:149px;top:1183px;font-size:19px}
.emp-lorem{left:148px;top:1222px;width:430px;font-size:14.2px;line-height:20px}

.app-phone{left:648px;top:1003px;width:206px;height:423px;background:var(--white);border:2px solid #d6d9dc;border-radius:26px;overflow:hidden;font-family:"Roboto",sans-serif}
.app-phone .bar{height:28px;font-size:8px;padding:10px 16px;color:#333}
.app-phone .org{display:flex;align-items:center;gap:6px;padding:4px 12px;font-size:8.5px;color:#444}
.app-phone .org i{width:14px;height:14px;border-radius:50%;background:var(--blue);display:inline-block}
.app-phone .search{margin:8px 12px;height:16px;border:1px solid #e4e6e8;font-size:7px;color:#aaa;padding:3px 5px}
.alert-row{margin:4px 12px;height:30px;background:var(--pale);border-left:3px solid var(--sky);display:flex;align-items:center;justify-content:space-between;padding:0 6px;font-size:7px;font-weight:700;color:#333}
.alert-row.b{border-left-color:var(--blue)}
.alert-row span.k{background:var(--sky);color:var(--navy);font-size:6px;padding:3px 6px;font-weight:500;white-space:nowrap}
.alert-row.b span.k{background:var(--blue);color:#fff}
.urgent-row{position:absolute;left:12px;width:178px;height:24px;background:var(--blue);color:#fff;font-size:7.5px;font-weight:700;display:flex;align-items:center;justify-content:space-between;padding:0 6px}
.urgent-row.sev{background:var(--navy)}
.urgent-row span{background:#fff;color:var(--navy);font-size:6px;padding:3px 6px;font-weight:500}

/* why */
.why{left:0;top:1549px;width:1200px;height:473px}
.why h2{position:absolute;top:10px;width:100%;text-align:center;font-size:46px;font-weight:700}
.why-col{position:absolute;width:260px;text-align:center;color:var(--white)}
.why-col h3{font-family:"Roboto",sans-serif;font-weight:700;font-size:19px;line-height:28px;margin-top:8px}
.why-col p{font-family:"Roboto",sans-serif;font-size:14.5px;line-height:20px}
.why-list{display:grid;grid-template-columns:auto auto;column-gap:26px;justify-content:center;text-align:left;font-family:"Roboto",sans-serif;font-size:14.5px;line-height:20px;margin-top:6px}
.why-list li{list-style:none}
.why-list li::before{content:"•";margin-right:14px}

/* scary */
.person-photo{left:0;top:2099px;width:378px;height:536px;background:linear-gradient(170deg,#b9bcbf 0%,#2b2f35 40%,#1f2328 100%)}
.map-soft{left:572px;top:2396px;width:260px;height:260px;border-radius:50%;background:radial-gradient(circle,#e6f1e4 0%,#eef5f2 60%,rgba(255,255,255,0) 72%)}
.desk-app{left:116px;top:2189px;width:521px;height:354px;background:var(--white);border:6px solid #e8eaec;font-family:"Roboto",sans-serif;font-size:8px;color:#444;overflow:hidden}
.desk-app .top{height:36px;border-bottom:1px solid #e4e6e8;display:flex;align-items:center;padding:0 12px;gap:18px;font-size:11px;letter-spacing:1px}
.desk-app .top i{width:28px;height:14px;background:#333;border-radius:7px;display:inline-block}
.desk-app .user{position:absolute;right:12px;top:9px;border:1px solid #ddd;padding:3px 8px;font-size:8px;letter-spacing:0}
.desk-app .side{position:absolute;left:10px;top:42px;width:150px;bottom:0;border-right:1px solid #eee}
.detail{display:grid;grid-template-columns:48px 1fr;row-gap:14px;margin-top:26px;padding-left:6px}
.note{position:absolute;left:210px;width:255px;height:52px;background:#fdf6dd;padding:8px 12px;font-size:7.5px;color:#888;font-style:italic}
.note b{display:block;font-style:normal;font-weight:400;color:#555;margin-top:14px}
.scary-title{left:657px;top:2196px;font-size:32px;font-weight:600;line-height:45px}
.scary-text{left:657px;top:2368px;width:420px;font-size:19px;line-height:27px}
.big-stat{left:659px;font-size:46px;font-weight:700;color:var(--blue);line-height:48px}
.big-stat small{font-size:24px;font-weight:600;color:var(--ink)}

/* plan */
.plan-title{left:0;top:2708px;width:1200px;text-align:center;font-size:47px;font-weight:600}
.step-num{position:absolute;top:2805px;width:36px;height:36px;border:1.5px solid var(--blue);border-radius:50%;color:var(--ink);font-size:21px;display:flex;align-items:center;justify-content:center}
.plan-card{position:absolute;top:2866px;width:264px;height:287px;background:var(--blue);color:var(--white);text-align:center;padding-top:40px}
.plan-card h3{font-size:25px;font-weight:700;line-height:31px}
.plan-card ul{list-style:none;margin:28px auto 0;text-align:left;display:inline-block;font-size:16px;line-height:22px}
.plan-card ul li::before{content:"•";margin-right:26px}
.plan-card p{font-size:16px;line-height:22px;padding:26px 30px 0}
.plan-card.mid{box-shadow:0 3px 10px rgba(0,0,0,.25)}

/* cta */
.cta{left:0;top:3308px;width:1200px;height:142px}
.cta p{position:absolute;left:177px;top:55px;font-family:"Roboto",sans-serif;font-weight:500;font-size:23px}

/* footer */
.foot-col{position:absolute;top:3482px;text-align:center;font-family:"Roboto",sans-serif}
.foot-col h4{font-size:22px;font-weight:700;margin-bottom:8px}
.foot-col ul{list-style:none;font-size:13.5px;line-height:20px;display:inline-grid;text-align:center}
.foot-col li{position:relative;padding-left:24px}
.foot-col li::before{content:"•";color:var(--blue);position:absolute;left:0}
.social{position:absolute;top:3568px;width:56px;height:56px;border-radius:50%;background:var(--blue)}
.legal-line{left:150px;top:3655px;width:900px;border-top:1px solid #c7cace}
.fine{position:absolute;top:3665px;font-family:"Roboto",sans-serif;font-size:13px}
</style>
</head>
<body>

<header class="site-header">
  <div class="brand" style="left:150px;top:12px;font-size:22px"><span class="dot" style="width:40px;height:40px"></span>CrewBeacon</div>
  <nav class="nav">
    <a class="active" style="left:502px">Home</a>
    <a style="left:569px">Buy Addons</a>
    <a style="left:677px">Cust Login</a>
  </nav>
  <a class="btn btn-outline" style="left:786px;top:13px;width:129px;height:41px">Sign In</a>
  <a class="btn btn-solid" style="left:921px;top:13px;width:128px;height:41px;font-weight:500">Sign Up</a>
</header>

<div class="abs hero-photo" role="img" aria-label="Hand pressing a compact panic button mounted under a desk"></div>
<section class="abs hero-band band">
  <h1>Feel Confident, Your Staff is Protected</h1>
  <p>Get a revolutionary new electronic panic button</p>
  <a class="btn btn-white" style="left:489px;top:95px;width:220px;height:42px;font-size:16px">Sign Up</a>
</section>

<div class="feature" style="left:140px">
  <svg viewBox="0 0 90 90" width="90"><path d="M22 48V24a5 5 0 0 1 10 0v18V14a5 5 0 0 1 10 0v28V12a5 5 0 0 1 10 0v30V18a5 5 0 0 1 10 0v40c0 16-10 28-24 28-12 0-18-8-24-18l-8-12a5 5 0 0 1 8-6z" fill="#1f7fc6"/></svg>
  <hr>
  <p>Problems Stopped Before They Start For Any Type Of Organization</p>
</div>
<div class="feature" style="left:484px">
  <svg viewBox="0 0 90 90" width="90"><circle cx="45" cy="45" r="44" fill="#1f7fc6"/><text x="45" y="62" text-anchor="middle" font-family="Open Sans" font-size="50" fill="#fff">$</text></svg>
  <hr>
  <p style="margin-top:4px">Affordable Prices Starting at $18per month. No Contracts. No Hidden Costs.</p>
</div>
<div class="feature" style="left:829px">
  <svg viewBox="0 0 90 90" width="90"><rect x="2" y="4" width="76" height="52" rx="3" fill="#1f7fc6"/><rect x="8" y="10" width="64" height="40" fill="#fff"/><rect x="30" y="56" width="20" height="8" fill="#1f7fc6"/><rect x="58" y="36" width="28" height="50" rx="4" fill="#1f7fc6" stroke="#fff" stroke-width="2"/><rect x="62" y="42" width="20" height="36" fill="#fff"/></svg>
  <hr>
  <p style="margin-top:4px">Alerts by computer, mobile device, text,phone, email, monitoring and E911</p>
</div>

<div class="abs pocket-photo" role="img" aria-label="Person taking a small panic button out of a jeans pocket"></div>
<h2 class="abs emp-title">Your Employees Shouldn’t Feel<br>Alone When They Need Help</h2>
<p class="abs emp-q">Does this problem make you feel frustrated and anxious?</p>
<p class="abs emp-q2">Put a simple solution in their hands</p>
<p class="abs emp-lorem">Lorem ipsum dolor sit amet, consectetur adipisicing elit, sed do eiusmod tempor incididunt ut labore et dolore magna aliqua. Ut enim ad minim veniam, quis nostrud exercitation ullamco laboris nisi ut aliquip ex ea commodo consequat. Duis</p>
<a class="btn btn-solid" style="left:148px;top:1352px;width:211px;height:51px">Get Started</a>

<div class="abs app-phone">
  <div class="bar">9:22</div>
  <div class="org"><i></i>KESTREL TOOLS</div>
  <div class="search">Search alerts</div>
  <div class="alert-row"><span>INTERNET DOWN. I CAN'T WORK</span><span class="k">Raise alert</span></div>
  <div class="alert-row b"><span>MAINTENANCE REQUEST</span><span class="k">Raise alert</span></div>
  <div class="urgent-row" style="top:310px">I NEED ASSISTANCE<span>Raise alert</span></div>
  <div class="urgent-row sev" style="top:344px">EMERGENCY<span>Raise alert</span></div>
</div>

<section class="abs why band">
  <h2>Why Businesses choose CrewBeacon</h2>
  <svg class="abs" style="left:290px;top:120px" width="620" height="60" viewBox="0 0 620 60" fill="none" stroke="#cfe5f5" stroke-width="1.5" stroke-dasharray="4 4"><path d="M8 50 Q110 -10 250 30"/><path d="M350 30 Q470 -10 605 40"/></svg>
</section>
<div class="why-col" style="left:123px;top:1676px">
  <svg width="56" height="60" viewBox="0 0 56 60"><path d="M14 28 L30 44 L42 30 L30 14 Z" fill="#fff"/><path d="M10 40 Q18 58 34 56 L44 42" fill="#fff"/><path d="M30 4 v8 M42 8 l-5 6 M18 8 l5 6" stroke="#fff" stroke-width="3"/></svg>
  <h3>EASY TO USE</h3>
  <p style="margin-top:42px">Press a button and let the right peopleknow you need help and open a chatwindow letting everyone talk on resolving their problem.</p>
</div>
<div class="why-col" style="left:457px;top:1676px">
  <svg width="64" height="60" viewBox="0 0 64 60"><rect x="4" y="6" width="26" height="20" rx="3" fill="#fff"/><circle cx="46" cy="14" r="9" fill="#fff"/><rect x="4" y="32" width="26" height="22" rx="3" fill="#fff"/><rect x="34" y="28" width="26" height="26" rx="4" fill="#fff"/></svg>
  <h3>COMMUNICATE THE WAY<br>YOU WANT</h3>
  <p style="margin-top:10px">We give you lots of options:</p>
  <ul class="why-list"><li>Computer</li><li>Text</li><li>Mobile</li><li>E911</li><li>Email</li><li>Call Center</li><li>Phone call</li></ul>
</div>
<div class="why-col" style="left:808px;top:1676px">
  <svg width="62" height="62" viewBox="0 0 62 62"><circle cx="31" cy="31" r="30" fill="#bfe0f7"/><text x="31" y="44" text-anchor="middle" font-family="Open Sans" font-size="34" fill="#1f7fc6">$</text></svg>
  <h3>COST EFFECTIVE<br>PROTECTION</h3>
  <p style="margin-top:16px">By leveraging your existing network and equipment we can lower your costs to give better options to your staff.</p>
</div>
<a class="btn btn-white" style="left:489px;top:1941px;width:218px;height:51px">Get Started</a>

<div class="abs person-photo" role="img" aria-label="Staff member wearing a panic button on a lanyard"></div>
<div class="abs map-soft" role="img" aria-label="Soft map graphic with a location marker"></div>
<div class="abs desk-app">
  <div class="top"><i></i>KESTREL TOOLS<span class="user">Dana Reyes ▾</span></div>
  <div class="side">
    <div style="padding:12px 0 0 2px">&lt;&lt; Go back to the list</div>
    <div style="text-align:center;margin-top:26px;font-size:20px">⚠</div>
    <div style="text-align:center;font-size:12px;margin-top:6px">Emergency</div>
    <div style="margin:22px auto 0;width:62px;border:1px solid var(--blue);color:var(--blue);text-align:center;padding:3px 0">End alert</div>
    <div class="detail"><span>Alert details:</span><span>8/8/2020</span><span></span><span>9:26 AM</span><span></span><span>Dana Reyes</span><span></span><span>210 Birch Lane, Fairview</span></div>
  </div>
  <div style="position:absolute;left:196px;top:54px">Alert chat:</div>
  <div class="note" style="top:72px">Text notifications were sent to: Lee Park.<b>HSN Notify System &nbsp; 9:26 AM</b></div>
  <div class="note" style="top:140px">Voice call notifications were sent to: 0 users.<b>HSN Notify System &nbsp; 9:26 AM</b></div>
  <div class="note" style="top:207px">Push notifications were sent to: 0 users.<b>HSN Notify System &nbsp; 9:26 AM</b></div>
  <div class="note" style="top:274px;left:224px;width:196px;background:#eef1f4;font-style:normal;color:#555">I am on my way<b>Lee Park &nbsp; 9:28 AM</b></div>
</div>
<h2 class="abs scary-title">We know how scary it<br>can feel to worry about<br>employee safety.</h2>
<p class="abs scary-text">That’s why we have provided a way for customers to get help to staff effectively in</p>
<div class="abs big-stat" style="top:2424px">45 States <small>covering</small></div>
<div class="abs big-stat" style="top:2468px">5 counteries</div>

<h2 class="abs plan-title">Simple Start Plan</h2>
<div class="step-num" style="left:263px">1</div>
<div class="step-num" style="left:581px">2</div>
<div class="step-num" style="left:898px">3</div>
<svg class="abs" style="left:350px;top:2813px" width="500" height="20" viewBox="0 0 500 20" fill="none" stroke="#1f7fc6" stroke-width="2"><path d="M0 10H176M168 3l8 7-8 7"/><path d="M319 10H497M489 3l8 7-8 7"/></svg>
<div class="plan-card" style="left:148px"><h3>Explore Your<br>Choices</h3><ul><li>Pricing</li><li>Trial</li><li>Quote</li><li>Hardware</li></ul></div>
<div class="plan-card mid" style="left:466px;padding-top:44px"><h3>Get Setup</h3><ul style="margin-top:34px"><li>Input Your Alerts</li><li>Input Your Staff</li><li>Install Our Software</li></ul></div>
<div class="plan-card" style="left:785px"><h3>Feel Confident Your<br>Staff Is Protected</h3><p>High Five. You just took a major step to get rid of the anxiety and frustration this gave you</p></div>
<a class="btn btn-solid" style="left:489px;top:3198px;width:218px;height:49px">Get Started</a>

<section class="abs cta band">
  <p>Stay Connected with Staff during a Crisis Situations</p>
  <a class="btn btn-white" style="left:771px;top:42px;width:249px;height:56px;font-size:24px;font-weight:400">Take free trial</a>
</section>

<footer>
  <div class="brand" style="left:150px;top:3508px;font-size:25px"><span class="dot" style="width:46px;height:46px"></span>CrewBeacon</div>
  <div class="abs" style="left:150px;top:3554px;width:322px;border-top:1.5px solid var(--blue)"></div>
  <span class="social" style="left:150px" role="img" aria-label="Video channel"></span>
  <span class="social" style="left:211px" role="img" aria-label="Microblog"></span>
  <span class="social" style="left:273px" role="img" aria-label="Professional network"></span>
  <span class="social" style="left:334px" role="img" aria-label="Social page"></span>
  <span class="social" style="left:396px" role="img" aria-label="Photo feed"></span>

  <div class="foot-col" style="left:500px;width:160px"><h4>Shop</h4><ul><li>Add Ons</li><li>Start My Demo</li><li>Custom Quote</li><li>Start Trial</li></ul></div>
  <div class="foot-col" style="left:680px;width:220px"><h4>About</h4>
    <div style="display:flex;gap:18px;justify-content:center">
      <ul><li>Affiliates</li><li>Contact</li><li>Support</li><li>Existing<br>Customers</li></ul>
      <ul style="align-self:start"><li>Industries</li><li>Blog</li><li>FAQ</li></ul>
    </div></div>
  <div class="foot-col" style="left:906px;width:180px"><h4>Legal</h4><ul><li>Privacy Policy</li><li>Terms of Use</li><li>End User License<br>Agreement</li></ul></div>

  <div class="abs legal-line"></div>
  <p class="fine" style="left:154px">©CrewBeacon 2020</p>
  <p class="fine" style="left:329px;width:520px;font-size:10px;line-height:14px">When employees feel alone during a threatening situation, we give them a way to let the right resources know that they need help so you can feel confident that your staff is protected.</p>
  <p class="fine" style="left:861px">Call Us : 1 – 800 – 555 – 0142</p>
</footer>

</body>
</html>
```